UX/UI Design of mobile application for language learning through picture cards

We are looking for a Mobile Application Designer with knowledge of UX/UI concepts.

We best candidate is a skilled Mobile Application Designer with knowledge of last trends and with experience in completing similar tasks.

This is a test task. After successful completion, the best candidate will be given a full task.

```html
<!DOCTYPE html>
<html lang="en">
<head>
<meta charset="utf-8">
<title>Picture Cards – Quiz Flow</title>
<link href="https://fonts.googleapis.com/css2?family=Inter:wght@400;500;600;700&display=swap" rel="stylesheet">
<style>
  :root {
    --canvas: #f4f5f9;
    --screen: #f3f4f9;
    --card: #ffffff;
    --ink: #2f3a4f;
    --ink-soft: #4a5264;
    --muted: #d9dce5;
    --primary: #5b50c0;
    --primary-deep: #4a40a8;
    --accent: #1fd3c6;
    --highlight: rgba(246, 178, 60, 0.55);
    --highlight-line: #f0a21e;
    --label: #f6a623;
    --photo-a: #f1f1f1;
    --photo-b: #d4d4d6;
    --photo-c: #3a3a3c;
  }
  * { box-sizing: border-box; margin: 0; padding: 0; }
  html, body { width: 1200px; height: 941px; overflow: hidden; }
  body {
    background: var(--canvas);
    font-family: "Inter", sans-serif;
    color: var(--ink);
    position: relative;
  }
  .screen {
    position: absolute;
    width: 275px;
    height: 596px;
    border-radius: 26px;
    background: var(--screen);
    box-shadow: 0 18px 40px rgba(60, 64, 110, 0.10);
    overflow: hidden;
  }
  .screen--question { left: 117px; top: 210px; }
  .screen--answer { left: 462px; top: 136px; }
  .screen--result { left: 808px; top: 210px; background: var(--primary); }

  .status-bar {
    position: absolute; left: 0; right: 0; top: 10px; height: 14px;
    display: flex; justify-content: space-between; align-items: center;
    padding: 0 18px 0 24px;
    font-size: 11px; font-weight: 600;
  }
  .screen--result .status-bar { color: #fff; }
  .back-arrow { position: absolute; left: 12px; top: 45px; }

  .question-title {
    position: absolute; left: 0; right: 0; top: 64px;
    text-align: center; font-size: 20px; font-weight: 600; line-height: 25px;
  }
  .picture {
    position: absolute; left: 11px; top: 136px; width: 252px; height: 200px;
    border-radius: 8px; overflow: hidden;
    background: linear-gradient(135deg, var(--photo-a) 0%, var(--photo-b) 55%, var(--photo-c) 100%);
    box-shadow: 0 8px 18px rgba(40, 40, 70, 0.12);
  }
  .picture__highlight {
    position: absolute; left: 61px; top: 14px; width: 170px; height: 141px;
    background: var(--highlight); border: 1.5px solid var(--highlight-line); border-radius: 6px;
  }
  .picture__tag {
    position: absolute; background: var(--label); color: #fff;
    font-size: 11px; font-weight: 600; border-radius: 6px;
    display: flex; align-items: center; justify-content: center;
  }
  .picture__tag--unknown { left: 50px; top: 25px; width: 22px; height: 22px; }
  .picture__tag--named { left: 31px; top: 24px; padding: 0 9px; height: 23px; font-size: 11.5px; }

  .options { position: absolute; left: 21px; top: 362px; width: 231px; }
  .option {
    height: 42px; background: var(--card); border-radius: 7px; margin-bottom: 8px;
    display: flex; align-items: center; padding: 0 12px; gap: 9px;
    font-size: 12px; color: var(--ink-soft);
    border: 1.5px solid transparent;
  }
  .option__radio { width: 17px; height: 17px; border-radius: 50%; border: 1.5px solid var(--muted); flex: none; }
  .option--correct { border-color: #b9f1ec; color: var(--accent); font-weight: 600;
    box-shadow: 0 4px 12px rgba(31, 211, 198, 0.15); }
  .option__check { width: 17px; height: 17px; flex: none; }

  .continue-button {
    position: absolute; left: 21px; top: 531px; width: 231px; height: 42px;
    background: var(--primary); border-radius: 7px; color: #fff;
    font-size: 12px; font-weight: 600; letter-spacing: 1.4px;
    display: flex; align-items: center; justify-content: center;
    box-shadow: 0 10px 20px rgba(91, 80, 192, 0.28);
  }
  .continue-button__icon {
    position: absolute; right: 10px; top: 10px; width: 22px; height: 22px;
    border-radius: 50%; background: var(--primary-deep);
    display: flex; align-items: center; justify-content: center;
  }

  .score-ring { position: absolute; left: 0; top: 40px; }
  .reward-illustration {
    position: absolute; left: 82px; top: 125px; width: 110px; height: 112px;
    border-radius: 40%;
    background: linear-gradient(135deg, #f5d6b3 0%, #e7b98f 60%, #d8d8e0 100%);
    opacity: 0.9;
  }
  .result-card {
    position: absolute; left: 22px; top: 360px; width: 231px; height: 213px;
    background: var(--card); border-radius: 18px; text-align: center;
  }
  .points-badge {
    position: absolute; left: 83px; top: 343px; width: 107px; height: 33px;
    background: var(--card); border-radius: 17px;
    display: flex; align-items: center; justify-content: center;
    color: var(--accent); font-size: 11px; font-weight: 700; letter-spacing: 1.2px;
    box-shadow: 0 4px 10px rgba(30, 30, 80, 0.12);
  }
  .result-card__title { margin-top: 38px; font-size: 18px; font-weight: 600; }
  .result-card__text { margin-top: 14px; font-size: 10.5px; line-height: 17.5px; color: var(--ink-soft); }
  .next-button {
    position: absolute; left: 95px; top: 148px; width: 41px; height: 41px;
    border-radius: 50%; background: var(--primary);
    display: flex; align-items: center; justify-content: center;
  }
</style>
</head>
<body>

<svg width="0" height="0" style="position:absolute">
  <defs>
    <symbol id="status-icons" viewBox="0 0 48 10">
      <rect x="0" y="7" width="2.5" height="3" rx=".5" fill="currentColor"/>
      <rect x="3.5" y="5" width="2.5" height="5" rx=".5" fill="currentColor"/>
      <rect x="7" y="3" width="2.5" height="7" rx=".5" fill="currentColor"/>
      <rect x="10.5" y="1" width="2.5" height="9" rx=".5" fill="currentColor"/>
      <path d="M17 4.2a7 7 0 0 1 9.5 0M18.6 6a4.6 4.6 0 0 1 6.3 0M20.4 7.8a2 2 0 0 1 2.7 0" stroke="currentColor" stroke-width="1.3" fill="none" stroke-linecap="round"/>
      <rect x="31" y="1.5" width="15" height="7" rx="1.8" fill="none" stroke="currentColor" stroke-width=".8"/>
      <rect x="32.3" y="2.8" width="12.4" height="4.4" rx="1" fill="currentColor"/>
    </symbol>
    <symbol id="arrow-left" viewBox="0 0 18 12">
      <path d="M17 6H2M6.5 1.5 2 6l4.5 4.5" stroke="currentColor" stroke-width="1.5" fill="none" stroke-linecap="round" stroke-linejoin="round"/>
    </symbol>
    <symbol id="arrow-right" viewBox="0 0 12 10">
      <path d="M1 5h10M7 1l4 4-4 4" stroke="currentColor" stroke-width="1.5" fill="none" stroke-linecap="round" stroke-linejoin="round"/>
    </symbol>
  </defs>
</svg>

<!-- Question screen -->
<section class="screen screen--question">
  <div class="status-bar"><span>9:41</span><svg width="48" height="10"><use href="#status-icons"/></svg></div>
  <svg class="back-arrow" width="18" height="12" style="color:var(--primary)"><use href="#arrow-left"/></svg>
  <h1 class="question-title">What is highlighted<br>in the picture?</h1>
  <div class="picture" role="img" aria-label="Desk photo with a camera, pencils, a cup of tea and a laptop">
    <div class="picture__highlight"></div>
    <div class="picture__tag picture__tag--unknown">?</div>
  </div>
  <div class="options">
    <div class="option"><span class="option__radio"></span>Laptop</div>
    <div class="option"><span class="option__radio"></span>Camera</div>
    <div class="option"><span class="option__radio"></span>Pen</div>
  </div>
  <div class="continue-button">Continue
    <span class="continue-button__icon"><svg width="12" height="10" style="color:#fff"><use href="#arrow-right"/></svg></span>
  </div>
</section>

<!-- Answer screen -->
<section class="screen screen--answer">
  <div class="status-bar"><span>9:41</span><svg width="48" height="10"><use href="#status-icons"/></svg></div>
  <svg class="back-arrow" width="18" height="12" style="color:var(--primary)"><use href="#arrow-left"/></svg>
  <h1 class="question-title">What is highlighted<br>in the picture?</h1>
  <div class="picture" role="img" aria-label="Desk photo with a camera, pencils, a cup of tea and a laptop">
    <div class="picture__highlight"></div>
    <div class="picture__tag picture__tag--named">Camera</div>
  </div>
  <div class="options">
    <div class="option"><span class="option__radio"></span>Laptop</div>
    <div class="option option--correct">
      <svg class="option__check" viewBox="0 0 17 17"><circle cx="8.5" cy="8.5" r="8.5" fill="var(--accent)"/><path d="M4.8 8.8 7.4 11.3 12.3 6" stroke="#fff" stroke-width="1.6" fill="none" stroke-linecap="round" stroke-linejoin="round"/></svg>
      Camera
    </div>
    <div class="option"><span class="option__radio"></span>Pen</div>
  </div>
  <div class="continue-button">Continue
    <span class="continue-button__icon"><svg width="12" height="10" style="color:#fff"><use href="#arrow-right"/></svg></span>
  </div>
</section>

<!-- Result screen -->
<section class="screen screen--result">
  <div class="status-bar"><span>9:41</span><svg width="48" height="10" style="color:#fff"><use href="#status-icons"/></svg></div>
  <svg class="back-arrow" width="18" height="12" style="color:#fff"><use href="#arrow-left"/></svg>
  <svg class="score-ring" width="275" height="290" viewBox="0 0 275 290">
    <circle cx="137" cy="141" r="126" fill="none" stroke="rgba(255,255,255,0.14)" stroke-width="1"/>
    <circle cx="137" cy="141" r="80" fill="#3f3592"/>
    <path d="M137 50 A91 91 0 0 0 137 232" fill="none" stroke="var(--accent)" stroke-width="16" stroke-linecap="round"/>
  </svg>
  <div class="reward-illustration" role="img" aria-label="3D illustration of a hand giving a thumbs up"></div>
  <div class="result-card">
    <h2 class="result-card__title">Correct!</h2>
    <p class="result-card__text">You are awesome!<br>Congratulations for getting the<br>answer correct!</p>
    <div class="next-button"><svg width="14" height="11" style="color:#fff"><use href="#arrow-right"/></svg></div>
  </div>
  <div class="points-badge">+25 POINTS</div>
</section>

</body>
</html>
```